Brightwire Hollow Business cards

one side I would like my logo (uploaded) and the other side I want my details. I'm an electrician in sydney. The logo side I'm happy with just a white background and our logo in the middle.

Details for other side
24/7 Sydney Electrician
Marcus Pell
0431 587 219
marcus@brightwirehollow.com.au
brightwirehollow.com.au
icons for facebook, instagram, linked in

Industry/Entity Type

electrician

Contact Information for Business Card

company info

```html
<!DOCTYPE html>
<html lang="en">
<head>
<meta charset="utf-8">
<title>Brightwire Hollow — Business Cards</title>
<link rel="stylesheet" href="https://fonts.googleapis.com/css2?family=Montserrat:wght@400;500;700;800&display=swap">
<style>
  :root {
    --backdrop: #d3d1d2;
    --paper: #ffffff;
    --ink: #141414;
    --signal-red: #ee3625;
    --white: #ffffff;
    --card-w: 540px;
    --card-h: 310px;
  }
  * { box-sizing: border-box; margin: 0; padding: 0; }
  html, body {
    width: 1200px; height: 900px; overflow: hidden;
    background: var(--backdrop);
    font-family: "Montserrat", sans-serif;
  }
  .canvas {
    position: relative; width: 1200px; height: 900px;
    display: flex; flex-direction: column; align-items: center; justify-content: center; gap: 50px;
  }
  .card {
    position: relative; width: var(--card-w); height: var(--card-h);
    overflow: hidden; box-shadow: 0 6px 18px rgba(0,0,0,0.18);
  }

  /* Logo side */
  .card--front { background: var(--paper); }
  .front__band {
    position: absolute; left: 0; right: 0; top: 196px; height: 20px; background: var(--ink);
  }
  .front__brand {
    position: absolute; left: 0; right: 0; top: 112px; text-align: center;
    font-weight: 800; font-size: 40px; letter-spacing: 0.5px; color: var(--ink);
  }
  .front__tagline {
    position: absolute; left: 130px; width: 280px; top: 184px; height: 44px;
    background: var(--signal-red); color: var(--white);
    display: flex; align-items: center; justify-content: center;
    font-weight: 500; font-size: 17px;
  }

  /* Details side */
  .card--back { background: var(--ink); }
  .back__split { position: absolute; inset: 0; }
  .back__brand {
    position: absolute; left: 0; width: 216px; top: 128px; text-align: center;
    color: var(--white); font-weight: 800; font-size: 24px; line-height: 1.15;
  }
  .back__details {
    position: absolute; left: 252px; top: 48px; right: 20px; color: var(--white);
  }
  .person__name { font-weight: 800; font-size: 26px; line-height: 1; white-space: nowrap; }
  .person__role {
    display: inline-block; margin-top: 4px; padding-bottom: 4px;
    font-size: 11px; letter-spacing: 0.5px; border-bottom: 1px solid var(--white);
  }
  .contact-list { list-style: none; margin-top: 18px; display: flex; flex-direction: column; gap: 14px; }
  .contact-list li { display: flex; align-items: center; gap: 10px; font-size: 13px; white-space: nowrap; }
  .contact-list svg { width: 18px; height: 18px; flex: none; }
  .social {
    position: absolute; right: 28px; bottom: 30px; display: flex; gap: 10px;
  }
  .social__dot { width: 24px; height: 24px; border-radius: 50%; background: var(--white); }
</style>
</head>
<body>
<main class="canvas">

  <section class="card card--front" aria-label="Business card, logo side">
    <div class="front__band"></div>
    <div class="front__brand">Brightwire Hollow</div>
    <div class="front__tagline">24/7 Sydney Electrician</div>
  </section>

  <section class="card card--back" aria-label="Business card, details side">
    <svg class="back__split" viewBox="0 0 540 310" width="540" height="310" aria-hidden="true">
      <rect x="216" y="0" width="324" height="310" fill="var(--signal-red)"/>
      <rect x="216" y="100" width="12" height="14" fill="var(--ink)"/>
      <rect x="216" y="206" width="12" height="14" fill="var(--ink)"/>
    </svg>

    <div class="back__brand">Brightwire<br>Hollow</div>

    <div class="back__details">
      <div class="person__name">Marcus Pell</div>
      <div class="person__role">MANAGER</div>
      <ul class="contact-list">
        <li>
          <svg viewBox="0 0 24 24"><circle cx="12" cy="12" r="12" fill="#fff"/><path d="M8.5 6.5l2 2.2-1.2 1.6c.8 1.7 2 2.9 3.7 3.7l1.6-1.2 2.2 2-1.4 1.9c-4-.6-7.5-4.1-8.2-8.2z" fill="var(--signal-red)"/></svg>
          0431 587 219
        </li>
        <li>
          <svg viewBox="0 0 24 24"><circle cx="12" cy="12" r="12" fill="#fff"/><rect x="6" y="8" width="12" height="8" rx="1" fill="none" stroke="var(--signal-red)" stroke-width="1.6"/><path d="M6.5 8.5l5.5 4 5.5-4" fill="none" stroke="var(--signal-red)" stroke-width="1.6"/></svg>
          marcus@brightwirehollow.com.au
        </li>
        <li>
          <svg viewBox="0 0 24 24"><path d="M12 3l10 9h-3v9h-5v-6h-4v6H5v-9H2z" fill="#fff"/></svg>
          brightwirehollow.com.au
        </li>
      </ul>
    </div>

    <div class="social" aria-label="Social media links">
      <span class="social__dot"></span>
      <span class="social__dot"></span>
      <span class="social__dot"></span>
    </div>
  </section>

</main>
</body>
</html>
```